Graphic to show easy steps to find financial clarity

Howdy-I need a graphic that describe my Coin Harbor Method.The attached is a concept, but please use your own creativity to show how you would display this:- There are 5 steps the process (and then we repeat/recalculate)- And three bullets that drive home the results of the processI've also attached my logo. Please use the colors in my logo and maybe add a soft green as needed.The reader should be able to briefly scan this document and understand that this is an easy/simple process that tells them how to manage their cash.Thanks!-Ned

Target Market(s)

wealthy women, whether single or married

Requirements
Must have
• Please use the colors in my logo and a soft green if needed
Should not have
• This should be a very easy to read graphic that communicates how simple/easy this is to do.

```html
<!DOCTYPE html>
<html lang="en">
<head>
<meta charset="utf-8">
<title>Coin Harbor Method</title>
<link href="https://fonts.googleapis.com/css2?family=Lato:wght@300;400;700;900&display=swap" rel="stylesheet">
<style>
  :root {
    --navy: #0b3a7e;
    --navy-ink: #0d2a5c;
    --blue: #3e6db0;
    --sky: #7fa6d6;
    --teal: #5bc3c9;
    --mint: #8fd3bd;
    --band: #8fa9d2;
    --grey-text: #555b63;
    --ring: #dcdde0;
    --page: #e9ebef;
    --white: #ffffff;
  }
  * { box-sizing: border-box; margin: 0; padding: 0; }
  html, body { width: 1200px; height: 1200px; overflow: hidden; background: var(--page); font-family: "Lato", Arial, sans-serif; }
  .sheet { position: absolute; left: 0; top: 176px; width: 1200px; height: 848px; }
  .sheet-body { position: absolute; left: 0; top: 18px; width: 1200px; height: 830px; background: var(--white); }
  .header-band { position: absolute; left: 0; top: 18px; width: 1200px; height: 92px; background: var(--navy); }
  .brand-box {
    position: absolute; left: 20px; top: 0; width: 338px; height: 125px; background: var(--white);
    box-shadow: 0 4px 10px rgba(0,0,0,0.25); display: flex; align-items: center; justify-content: center; gap: 12px;
  }
  .brand-mark { width: 26px; height: 26px; background: var(--navy); }
  .brand-name { color: var(--navy); font-weight: 700; font-size: 27px; letter-spacing: 0.5px; }
  .title {
    position: absolute; left: 358px; right: 0; top: 18px; height: 92px; display: flex; align-items: center; justify-content: center;
    color: var(--white); font-size: 52px; letter-spacing: 0.5px;
  }
  .title strong { font-weight: 900; margin-right: 14px; }
  .title span { font-weight: 300; }
  .flow { position: absolute; left: 0; top: 0; width: 1200px; height: 848px; }
  .repeat { position: absolute; left: 651px; width: 280px; top: 146px; text-align: center; color: var(--navy); }
  .repeat h2 { font-size: 40px; font-weight: 900; line-height: 1; }
  .repeat p { font-size: 20px; font-weight: 700; margin-top: 10px; color: var(--navy); }
  .step { position: absolute; top: 512px; width: 180px; margin-left: -90px; text-align: center; color: var(--grey-text); font-size: 19px; line-height: 24px; }
  .step h3 { font-size: 22px; font-weight: 900; text-decoration: underline; text-underline-offset: 6px; text-decoration-thickness: 3px; margin-bottom: 16px; }
  .step b { font-weight: 900; }
  .step-1 { left: 230px; } .step-1 h3 { color: var(--navy); }
  .step-2 { left: 421px; } .step-2 h3 { color: var(--blue); }
  .step-3 { left: 613px; } .step-3 h3 { color: var(--sky); }
  .step-4 { left: 805px; } .step-4 h3 { color: var(--teal); }
  .step-5 { left: 996px; } .step-5 h3 { color: var(--mint); }
  .results-band { position: absolute; left: 0; top: 666px; width: 1200px; height: 123px; background: var(--band); }
  .results-check { position: absolute; left: 129px; top: 14px; width: 72px; height: 84px; }
  .results-list { position: absolute; left: 213px; top: 22px; list-style: none; color: var(--white); font-size: 18px; line-height: 26px; }
  .results-list li::before { content: "• "; }
  .footer-band { position: absolute; left: 0; top: 789px; width: 1200px; height: 59px; background: var(--navy); display: flex; align-items: center; justify-content: center; color: var(--white); font-weight: 900; font-size: 22px; }
</style>
</head>
<body>
<main class="sheet">
  <div class="sheet-body"></div>
  <div class="header-band"></div>
  <div class="title"><strong>COIN HARBOR</strong><span>METHOD</span></div>
  <div class="brand-box"><div class="brand-mark"></div><div class="brand-name">Harborline Wealth</div></div>

  <svg class="flow" viewBox="0 0 1437 1015" aria-hidden="true">
    <defs>
      <linearGradient id="waveGrad" gradientUnits="userSpaceOnUse" x1="150" y1="0" x2="1330" y2="0">
        <stop offset="0" stop-color="#0b3a7e"/>
        <stop offset="0.35" stop-color="#2f5ea6"/>
        <stop offset="0.6" stop-color="#7fa6d6"/>
        <stop offset="0.8" stop-color="#5bc3c9"/>
        <stop offset="1" stop-color="#8fd3bd"/>
      </linearGradient>
      <filter id="softShadow" x="-20%" y="-20%" width="140%" height="140%">
        <feDropShadow dx="0" dy="3" stdDeviation="4" flood-color="#000" flood-opacity="0.2"/>
      </filter>
    </defs>
    <path d="M1307.75 452 L1307.75 330 A80 80 0 0 0 1227.75 250 L600 250" fill="none" stroke="#8fd3bd" stroke-width="40"/>
    <polygon points="607,198 607,270 494,270" fill="#8fd3bd"/>
    <path d="M275 337.5 A114.5 114.5 0 0 0 160.5 452 A114.5 114.5 0 0 0 389.5 452 A114.5 114.5 0 0 1 618.5 452 A114.5 114.5 0 0 0 847.5 452 A114.5 114.5 0 0 1 1077.5 452 A115 115 0 0 0 1307.75 452" fill="none" stroke="url(#waveGrad)" stroke-width="40"/>

    <g filter="url(#softShadow)" fill="#ffffff" stroke="#dcdde0" stroke-width="7">
      <circle cx="275" cy="452" r="88"/>
      <circle cx="504.5" cy="452" r="88"/>
      <circle cx="734" cy="452" r="88"/>
      <circle cx="963.5" cy="452" r="88"/>
      <circle cx="1193" cy="452" r="88"/>
    </g>

    <g fill="none" stroke="#0d2a5c" stroke-width="6" stroke-linecap="round" stroke-linejoin="round">
      <!-- step 1: cycle with dollar -->
      <path d="M235 440 A42 42 0 0 1 305 420"/>
      <polyline points="296,408 307,420 292,428"/>
      <path d="M315 464 A42 42 0 0 1 245 484"/>
      <polyline points="254,496 243,484 258,476"/>
      <!-- step 2: receipt -->
      <rect x="458" y="408" width="88" height="12" rx="3"/>
      <path d="M470 420 V492 H540 V420"/>
      <line x1="484" y1="478" x2="526" y2="478"/>
      <!-- step 3: calendar -->
      <rect x="692" y="420" width="84" height="76" rx="6"/>
      <line x1="692" y1="440" x2="776" y2="440"/>
      <line x1="712" y1="410" x2="712" y2="428"/>
      <line x1="756" y1="410" x2="756" y2="428"/>
      <!-- step 4: savings jar -->
      <path d="M930 440 H998 V490 A8 8 0 0 1 990 498 H938 A8 8 0 0 1 930 490 Z"/>
      <line x1="950" y1="440" x2="978" y2="440"/>
      <rect x="940" y="428" width="48" height="12" rx="3"/>
      <!-- step 5: sprout -->
      <line x1="1193" y1="446" x2="1193" y2="506"/>
      <path d="M1193 490 C1175 470 1158 475 1150 480 C1160 495 1180 497 1193 490"/>
      <path d="M1193 490 C1211 470 1228 475 1236 480 C1226 495 1206 497 1193 490"/>
      <circle cx="1193" cy="422" r="26"/>
    </g>
    <g fill="#0d2a5c" font-family="Lato, Arial, sans-serif" font-weight="900" text-anchor="middle">
      <text x="275" y="470" font-size="52">$</text>
      <text x="505" y="462" font-size="36" fill="#3e6db0">$</text>
      <text x="734" y="412" font-size="22" fill="#3e6db0">5Y</text>
      <text x="964" y="480" font-size="30" fill="#5bc3c9">$</text>
      <text x="1193" y="433" font-size="30" fill="#5bc3c9">$</text>
    </g>
    <g fill="#0d2a5c">
      <rect x="704" y="452" width="10" height="9"/><rect x="720" y="452" width="10" height="9"/><rect x="736" y="452" width="10" height="9"/><rect x="752" y="452" width="10" height="9"/>
      <rect x="704" y="470" width="10" height="9"/><rect x="720" y="470" width="10" height="9"/><rect x="736" y="470" width="10" height="9"/><rect x="752" y="470" width="10" height="9"/>
    </g>
  </svg>

  <div class="repeat"><h2>REPEAT</h2><p>RECALCULATE MONTHLY</p></div>

  <section class="step step-1"><h3>STEP 1</h3><p>KNOW<br>YOUR <b>ANNUAL</b><br>SPENDING</p></section>
  <section class="step step-2"><h3>STEP 2</h3><p>PROJECT<br><b>SPECIAL</b><br><b>EXPENSES</b></p></section>
  <section class="step step-3"><h3>STEP 3</h3><p>ADD UP<br>YOUR <b>5 YEAR</b><br>CASH NEEDS</p></section>
  <section class="step step-4"><h3>STEP 4</h3><p>SET THEM<br>ASIDE IN<br><b>SAVINGS</b></p></section>
  <section class="step step-5"><h3>STEP 5</h3><p><b>INVEST</b><br>THE REST</p></section>

  <div class="results-band">
    <svg class="results-check" viewBox="0 0 72 84" aria-hidden="true">
      <rect x="3" y="24" width="56" height="56" fill="none" stroke="#ffffff" stroke-width="5"/>
      <path d="M14 50 L28 66 L68 6" fill="none" stroke="#ffffff" stroke-width="9" stroke-linejoin="round"/>
    </svg>
    <ul class="results-list">
      <li>KNOW YOUR LIFESTYLE WILL BE UNAFFECTED BY THE MARKETS FOR AT LEAST 5 YEARS</li>
      <li>SPEND INTENTIONALLY AND WITH JOY</li>
      <li>CREATE A SOLID BASE FOR LIFETIME CASH FLOW PROJECTIONS</li>
    </ul>
  </div>
  <footer class="footer-band">www.harborlinewealth.com</footer>
</main>
</body>
</html>
```